Business Promotion A1 Poster

I need an A1 poster for a lift in my building. It needs to promote BrightlineHub aa an employment expert for small business wanting to get their employment stuff right. We do on-site employment audits in Wellington for free.

We help small business manage the new 90 day trial period and help them design office/business policy manuals to avoid workplace problems.

The final design needs to convey expert and experience in employment. We use orange and grey as corporate colours. The company logo can be found on our website www.brightlinehub.co.nz

Target Market(s)

Small business owners and managers

Industry/Entity Type

Small Business

Requirements
Nice to have
• colour information experts employment law in NZ

```html
<!DOCTYPE html>
<html lang="en">
<head>
<meta charset="utf-8">
<title>BrightlineHub – Employment Knowledge Poster</title>
<link href="https://fonts.googleapis.com/css2?family=Arimo:ital,wght@0,400;0,700;1,700&display=swap" rel="stylesheet">
<style>
  :root {
    --orange: #f7941d;
    --orange-text: #f39a25;
    --peach: #fcca8d;
    --grey: #8a8a8a;
    --ink: #1a1a1a;
    --white: #ffffff;
  }
  * { margin: 0; padding: 0; box-sizing: border-box; }
  html, body { width: 900px; height: 1200px; overflow: hidden; background: var(--white); }
  body { font-family: "Arimo", Arial, sans-serif; color: var(--ink); position: relative; }

  .hero { position: absolute; left: 19px; top: 0; width: 862px; height: 447px; background: var(--peach); }
  .photo { position: absolute; }
  .photo--consultant { left: 20px; top: 108px; width: 257px; height: 176px; background: linear-gradient(135deg, #c98a3f, #e9c7a0 55%, #4a4f5a); }
  .photo--team { left: 260px; top: 0; width: 189px; height: 123px; background: linear-gradient(160deg, #f47b20, #d9c2ae 60%, #2e2f36); }
  .photo--support { left: 449px; top: 45px; width: 182px; height: 155px; background: linear-gradient(135deg, #9fb4c8, #e9cdb7 55%, #7a4a2c); }
  .photo--site { left: 602px; top: 154px; width: 242px; height: 164px; background: linear-gradient(180deg, #f08a1c, #e46c10 60%, #2a1a10); }
  .photo--workforce { left: 290px; top: 200px; width: 282px; height: 220px; background: linear-gradient(180deg, #ffffff, #d8d6d3 45%, #f2f2f2); }

  .tagline { position: absolute; left: 0; top: 365px; width: 900px; text-align: center;
    font-size: 25.5px; font-weight: 700; font-style: italic; color: var(--orange); }

  .brand-band { position: absolute; left: 0; top: 479px; width: 900px; height: 87px; }
  .brand-band__bar { position: absolute; left: 252px; top: 0; right: 0; height: 87px; background: var(--orange); }
  .brand-name { position: absolute; left: 25px; top: 23px; font-size: 32px; font-weight: 400; color: var(--grey); white-space: nowrap; }

  .services { position: absolute; left: 18px; top: 596px; width: 864px; height: 401px;
    border: 4px solid var(--orange); border-radius: 14px; }
  .column { position: absolute; top: 14px; font-size: 12.5px; line-height: 16px; }
  .column--about { left: 12px; width: 250px; }
  .column--experts { left: 295px; width: 260px; }
  .column--tools { left: 591px; width: 258px; }
  .column h2 { font-size: 14px; font-weight: 700; color: var(--orange-text); text-align: center; line-height: 23px; margin-bottom: 12px; }
  .column--experts h2 { line-height: 17px; margin-bottom: 23px; }
  .column p { margin-bottom: 14px; }
  .director { color: var(--orange-text); }
  .column .packages { color: var(--orange-text); font-weight: 700; font-size: 14px; text-align: center; line-height: 17px; margin-top: 10px; }

  .contact { position: absolute; left: 0; top: 1043px; width: 900px; text-align: center;
    font-size: 16px; font-weight: 700; color: var(--orange-text); }

  .footer-brand { position: absolute; left: 0; top: 1138px; width: 900px; height: 48px; }
  .footer-brand__bar { position: absolute; left: 430px; top: 0; right: 0; height: 48px; background: var(--orange); }
  .footer-brand__name { position: absolute; left: 270px; top: 10px; font-size: 24px; color: var(--grey); white-space: nowrap; }
</style>
</head>
<body>
  <section class="hero">
    <div class="photo photo--consultant" role="img" aria-label="Photo of a smiling businesswoman holding folders in an office"></div>
    <div class="photo photo--team" role="img" aria-label="Photo of a group of business professionals"></div>
    <div class="photo photo--support" role="img" aria-label="Photo of a smiling woman with a headset at a computer"></div>
    <div class="photo photo--site" role="img" aria-label="Photo of construction workers silhouetted against orange scaffolding"></div>
    <div class="photo photo--workforce" role="img" aria-label="Photo of a diverse workforce standing together"></div>
  </section>
  <p class="tagline">empowering workplaces with employment knowledge</p>

  <header class="brand-band">
    <span class="brand-name">BrightlineHub</span>
    <div class="brand-band__bar"></div>
  </header>

  <main class="services">
    <div class="column column--about">
      <h2>You need BrightlineHub to help with your business</h2>
      <p>Contact BrightlineHub for a free on-site employment audit in Wellington or the 90 day trial period.</p>
      <p><span class="director">Dr Hana Whitcombe</span> - Director and Owner</p>
      <p>•Experience in recruitment and employment - designs templates for you to use to keep staff employment files up to date and easy to manage</p>
      <p>•You can have an on-site visit at no extra charge</p>
      <p>•You can have BrightlineHub do your in-house HR or buy templates to do it yourself</p>
      <p>•You can buy business tools on line</p>
    </div>
    <div class="column column--experts">
      <h2>The experts in employment and recruiting</h2>
      <p>BrightlineHub works for small businesses in New Zealand. You need BrightlineHub to help your business to:</p>
      <p>•Stay within New Zealand employment law requirements</p>
      <p>•Proof read or design your employment agreements</p>
      <p>•Help you manage the 90 day trial period easily</p>
      <p>•Help you organise and develop your employment systems</p>
      <p>•We are the education arm of Harlow Law - the employment law specialist</p>
    </div>
    <div class="column column--tools">
      <h2>You can use business tools in your business</h2>
      <p>Designed to help small business get the recruitment stuff right:</p>
      <p>•We build clear and straightforward employment agreements</p>
      <p>•We have a 90 day booklet to help you get the first 90 days right</p>
      <p>•We make sure your employment agreements comply with the most up-to-date legislation</p>
      <p>•We have DIY templates to let you check your current agreements on-line</p>
      <p class="packages">These packages include advice, reviews, and audits</p>
    </div>
  </main>

  <p class="contact">Level 4, 18 Kowhai Street, Wellington 6011&nbsp; Phone:04 555 0142&nbsp; Fax:04 555 0143</p>

  <footer class="footer-brand">
    <span class="footer-brand__name">BrightlineHub</span>
    <div class="footer-brand__bar"></div>
  </footer>
</body>
</html>
```